2-Page Flyer for the Information Session about the Tranquil Venture Course

This is a flyer to announce/advertise an evening Information Session about the Tranquil Venture Course. This Program aims at mindfully rethinking and redesigning work (and life) for people who feel stuck or not entirely satisfied with their work and/or life (please see draft flyer attached for more details). This Program is property of Brightfold Joy, a company that uses a combination of Mindfulness, Design, and Entrepreneurship to help people achieve greater happiness (in their work and lives).
Updates

Target Market(s)

People who feel stuck or not entirely satisfied with their work and/or life (please see draft flyer attached for more details)

Font styles to use
Serif
Sans Serif

Colors
ffffff
f37122
33a6d7
acd037

Requirements
Must have
• All of what I will say below is suggestive (I’m not a design expert), and I’m open to divert from it, if it makes sense and feels more interesting.
• I thought initially of a 2-page flyer (please see draft flyer attached). The first page could help people grasp the essence of the event quickly (in 1 or 2 minutes), and then, if they are interested/motivated, they would continue reading through page 2, which has more info about the Program in itself.
• Potential Structure
• Page 1
• . About the Information Session on the Tranquil Venture Course
• . Visible Date & Time, Contacts, Venue (and other relevant info)
• . About me (the facilitator)
• Page 2
• . About the Tranquil Venture Course
• I include a Powerpoint draft of the flyer with the content. The design is rudimentary and precarious from an aesthetics/organization point of view, and this is mainly where I need help (and maybe in other aspects too!).
• On the flyer, I would like to include:
• . A photo of myself (I attach 1 picture).
• . 1 or 2 beautiful-nature photos (cropped or full). One may have to do with looking at the sky, dreaming, and imagining a new work and life (2 photos with sky and clouds attached). The other has to do with walking the transformation journey (the photo with the person walking through the forest path).
• . brightfold joy logo or logos (there are two slightly different ones, that can be used for different purposes). For the first page, I would like the brightfold joy logo that has "brightfold joy" written on the bottom, with the saying "Stillness, Craft and Venture for Joy" beneath. This is the main logo. For the 2nd page, you can choose the logo that adapts better.
• - Where it says the "the way out is in" it would be great to have a similar font to the one I attach (see file "Font_the_way_out_is_in.png" and Ankecallig-fg.ttf
Nice to have
• In terms of colours, I would not divert much from the logo colours (and of course white and black). I would like the flyer to be quite white. Almost like fairy-tale white: the white horse, the white snow, the white of the stars, the white heaven. White could be the base colour. White means peace, tranquillity, calm contentment, a smile.
• And then use the other colours. The green of the mindfulness. The blue of the sky, the dreams. And the orange of the sun, the energy, the fire, the action. And maybe the black for text.
• Where it says the "the way out is in" it would be great to have a similar font to the one I attach (see file "Font_the_way_out_is_in".
• I would like this flyer to be a piece of art, in every possible way. Simple, beautiful, ease, light, peaceful, calm happy. Just like the Tranquil Venture Course and brightfold joy Company that I am creating intends to be. The mission of this Program and Company is to be a designer, a painter (a Picasso) of happier and more fulfilling human lives.
• I am very much looking forward to seeing your proposal(s).

```html
<!DOCTYPE html>
<html lang="en">
<head>
<meta charset="utf-8">
<title>Tranquil Venture Course – Information Session Flyer</title>
<link rel="stylesheet" href="https://fonts.googleapis.com/css2?family=Poppins:ital,wght@0,300;0,400;0,500;0,600;0,700;1,400;1,600&family=Rubik:wght@700&family=Roboto+Condensed:wght@400;700&family=Open+Sans:ital,wght@1,600&family=Satisfy&display=swap">
<style>
:root{
  --board:#3a3c3f;
  --paper:#ffffff;
  --orange:#f37122;
  --blue:#33a6d7;
  --blue-deep:#2f8fc6;
  --green:#acd037;
  --ink:#2b2b2b;
  --grey:#555;
}
*{margin:0;padding:0;box-sizing:border-box}
html,body{width:1200px;height:782px;overflow:hidden}
body{background:var(--board);font-family:"Poppins",sans-serif;color:var(--ink);position:relative}
.side-label{position:absolute;top:38px;width:443px;text-align:center;color:#fff;font:500 26px "Poppins",sans-serif;letter-spacing:1px}
.page{position:absolute;top:95px;width:443px;height:622px;background:var(--paper);overflow:hidden;box-shadow:0 6px 22px rgba(0,0,0,.45)}
.page > *{position:absolute}
.front{left:92px}
.back{left:651px}
.label-front{left:92px}.label-back{left:651px}

/* brand */
.brand-dot{border-radius:50%;background:var(--orange)}
.brand-name{font-family:"Poppins",sans-serif;font-weight:400;color:var(--blue);line-height:1}
.tagline{font-size:6.4px;color:var(--ink);width:100%;text-align:center}

/* front */
.title-box{left:48px;top:101px;width:347px;height:60px;border:1px solid var(--blue);border-radius:14px;text-align:center}
.title-main{font:700 21px "Rubik",sans-serif;color:var(--orange);margin-top:6px;letter-spacing:.3px}
.title-sub{font:300 20px "Poppins",sans-serif;color:var(--blue);line-height:1.1}
.session-tag{left:140px;top:171px;width:164px;height:20px;background:var(--green);color:#fff;font:700 14px "Roboto Condensed",sans-serif;text-align:center;line-height:20px;box-shadow:2px 2px 0 #cfd9b5}
.date-block{left:132px;top:202px;width:180px;height:34px;border-top:1px dotted #888;border-bottom:1px dotted #888;text-align:center;font-family:"Roboto Condensed",sans-serif;color:#444}
.date-line{font-size:11.5px;margin-top:3px}
.date-line b,.time-line{color:var(--orange);font-weight:700}
.time-line{font-size:11.5px;line-height:1.1}
.section-tab{background:var(--blue);color:#fff;font:700 10px "Roboto Condensed",sans-serif;line-height:17px;padding-left:6px;box-shadow:3px 3px 0 #d6d6d6}
.body-text{font-size:6.6px;line-height:1.25;color:var(--ink)}
.facilitator{left:25px;top:363px;font:700 11px "Roboto Condensed",sans-serif;color:var(--orange);white-space:nowrap}
.facilitator em{font:italic 600 10.5px "Open Sans",sans-serif;color:#3d4a55;margin-left:3px}
.bio-card{left:25px;top:383px;width:393px;height:129px;background:var(--blue);box-shadow:0 6px 6px -4px rgba(0,0,0,.35)}
.bio-photo{position:absolute;left:6px;top:9px;width:116px;height:108px;background:linear-gradient(160deg,#e4dfe0 0%,#c9bfc2 55%,#3c4656 100%);border:1px solid #fff}
.bio-text{position:absolute;left:134px;top:8px;width:250px;font-size:6.6px;line-height:1.3;color:#fff;text-align:justify}
.pill{background:var(--green);border-radius:9px;color:#fff;text-align:center;font-size:8.5px;font-weight:400}
.pill b{font-weight:600}
.booking{left:0;top:562px;width:100%;text-align:center;font-size:7.6px;line-height:1.55}
.booking .hd{color:var(--blue);font-weight:600}
.booking span.k{color:var(--blue);font-weight:600}
.venue-band{left:0;top:597px;width:443px;height:25px}
.venue-text{left:0;top:597px;width:380px;height:25px;line-height:25px;text-align:center;color:#fff;font-size:9px}
.venue-text b{font-weight:600}

/* back */
.sky{left:0;top:68px;width:443px;height:77px;background:linear-gradient(180deg,#bfe6f7 0%,#e6f5fc 45%,#8fcbea 100%)}
.sky-title{left:22px;top:80px;font:700 12.5px "Roboto Condensed",sans-serif;color:#222}
.sky-text{left:22px;top:101px;width:374px;font-size:6.6px;line-height:1.3;text-align:justify;color:#222}
.program-box{left:16px;top:177px;width:193px;height:118px;border:1px solid var(--orange);border-radius:12px}
.program-tab{left:16px;top:177px;width:97px;height:24px;background:var(--blue);color:#fff;font:700 12px "Roboto Condensed",sans-serif;line-height:24px;padding-left:9px;border-radius:12px 0 18px 0}
.program-text{left:24px;top:205px;width:177px;font-size:6.6px;line-height:1.3;text-align:justify}
.side-tab{height:18px;background:var(--blue);color:#fff;font:700 12.5px "Roboto Condensed",sans-serif;line-height:18px;padding-left:6px;border-radius:0 9px 9px 0}
.list{list-style:none}
.list li{display:flex;gap:3px;font-size:6.6px;line-height:1.25;margin-bottom:4px}
.num{flex:0 0 10px;height:10px;border-radius:50%;color:#fff;font-size:6px;font-weight:600;text-align:center;line-height:10px}
.num-blue{background:var(--blue)}.num-orange{background:var(--orange)}
.divider{left:215px;top:358px;height:131px;border-left:1px dashed #999}
.forest{left:0;top:505px;width:443px;height:117px;background:linear-gradient(180deg,#6b5a3e 0%,#3e3524 45%,#5a4a2e 75%,#2f2a1d 100%)}
.quote{left:0;top:504px;width:100%;text-align:center;font:27px "Satisfy",cursive;color:#1e1e1e}
.back-contact{left:0;top:585px;width:100%;text-align:center;color:#fff;font-size:7.6px}
.back-contact b{font-weight:600}
.back-pill{left:126px;top:604px;width:190px;height:13px;line-height:13px;font-size:7.6px}
</style>
</head>
<body>

<div class="side-label label-front">FRONT</div>
<div class="side-label label-back">BACK</div>

<!-- Page 1 -->
<section class="page front">
  <div class="brand-dot" style="left:211px;top:18px;width:22px;height:22px"></div>
  <div class="brand-name" style="left:0;top:52px;width:100%;text-align:center;font-size:16px">brightfold joy</div>
  <p class="tagline" style="left:0;top:78px">Stillness, Craft and Venture for Joy</p>

  <div class="title-box">
    <div class="title-main">TRANQUIL VENTURE</div>
    <div class="title-sub">COURSE</div>
  </div>

  <div class="session-tag">INFORMATION SESSION</div>

  <div class="date-block">
    <div class="date-line">Thursday <b>5th</b> September <b>2019</b></div>
    <div class="time-line">19:30 to 21:00</div>
  </div>

  <div class="section-tab" style="left:22px;top:254px;width:127px;height:17px">INFORMATION SESSION</div>
  <p class="body-text" style="left:24px;top:280px;width:395px">The purpose of this Information Session is to give you a real insight into the Tranquil Venture Course and how it can help you get the most out of your work and life.</p>

  <div class="section-tab" style="left:22px;top:304px;width:94px;height:17px">WHO CAN COME</div>
  <p class="body-text" style="left:24px;top:329px;width:395px">The Information Session is free. Whether you come on your own, or with friends or family, you'll be warmly welcome. It will take place on Thursday the 5th September 2019, from 19:30 to 21:00, at Kaleo Coworking. Please get in touch for more info or to book a place.</p>

  <div class="facilitator">FACILITATOR:<em>Dr Tomas Ferreira, Visiting Research Fellow, Northgate University</em></div>

  <div class="bio-card">
    <div class="bio-photo" role="img" aria-label="Portrait photo of the facilitator"></div>
    <p class="bio-text">Tomas joined Northgate University (School of Management) as a Lecturer in Entrepreneurship in 2015. He completed his PhD in Entrepreneurship at Harbourline Business School in 2014. His work received the Lindqvist Doctoral Dissertation Award from the Society for Management Studies. He began his business career as a production engineer (Voltaris), and continued in sales (Kranwerk). After his MBA, he worked as a strategy consultant at Riverside Business School. Originally from Portugal, Tomas enjoys designing and launching new ideas, international communities, mindfulness retreats, and musical improvisation. He nurtures a close connection to Quiet Pine Mindfulness Centre, where he has practiced and volunteered over 9 months. He has a broad experience of sharing the benefits of mindfulness with others.</p>
  </div>

  <div class="pill" style="left:52px;top:536px;width:340px;height:16px;line-height:16px"><b>More about the facilitator:</b> www.profiles.example/tferreira</div>

  <div class="booking">
    <div class="hd">Information &amp; Booking</div>
    <div><span class="k">Email:</span> info@brightfoldjoy.io</div>
    <div><span class="k">Tel:</span> +34 611 482 305 <i>(video call and messaging)</i></div>
  </div>

  <svg class="venue-band" viewBox="0 0 443 25" aria-hidden="true">
    <rect width="443" height="25" fill="var(--green)"/>
    <path d="M0 0H340C352 0 358 10 359 25H0Z" fill="var(--orange)"/>
    <path d="M340 0C352 0 358 10 359 25" fill="none" stroke="#fff" stroke-width="1"/>
  </svg>
  <div class="venue-text"><b>Venue:</b> Kaleo Coworking, C/ Olivera 42, Barcelona</div>
</section>

<!-- Page 2 -->
<section class="page back">
  <div class="brand-dot" style="left:164px;top:22px;width:30px;height:30px"></div>
  <div class="brand-name" style="left:203px;top:20px;font-size:15px;line-height:1">brightfold<br>joy</div>

  <div class="sky" role="img" aria-label="Soft blue sky with white clouds"></div>
  <h2 class="sky-title">What is Tranquil Venture</h2>
  <p class="sky-text">Being mindful means being aware and awake. Venture is the creation of a new form of organising. Tranquil Venture is then the process of creating or redesigning your work and life with awareness, in a way that is reflective of you, of your passions and values, thus conducing to a greater sense of fulfilment and happiness.</p>

  <div class="program-box"></div>
  <div class="program-tab">THE PROGRAM</div>
  <p class="program-text"><b>The Tranquil Venture Course</b> is a <b>4-month long transformative journey</b> designed for people who feel stuck or not entirely satisfied with their work and/or life. It is of benefit for everyone, at any stage. The Program consists of a 5-hour workshop each month, with 2-hour weekly peer support meetings. It combines mindfulness techniques, design thinking methodology, and venture frameworks.</p>

  <svg style="left:0;top:0;width:443px;height:622px" viewBox="0 0 443 622" aria-label="Cycle of four workshops joined by weekly peer support meetings" role="img">
    <g font-family="Poppins, sans-serif" text-anchor="middle" fill="#fff" font-weight="600" font-size="6">
      <circle cx="322" cy="194" r="28" fill="var(--orange)"/>
      <text x="322" y="189">Workshop 1</text><text x="322" y="196">INSIGHT</text><text x="322" y="204">(5 hours)</text>
      <circle cx="377" cy="238" r="28" fill="var(--blue)"/>
      <text x="377" y="233">Workshop 2</text><text x="377" y="240">DESIGN</text><text x="377" y="248">(5 hours)</text>
      <circle cx="322" cy="284" r="28" fill="var(--green)"/>
      <text x="322" y="279">Workshop 3</text><text x="322" y="286">EXECUTE</text><text x="322" y="294">(5 hours)</text>
      <circle cx="268" cy="239" r="28" fill="#4f93c0"/>
      <text x="268" y="234">Workshop 4</text><text x="268" y="241">PRESENT</text><text x="268" y="249">(5 hours)</text>
    </g>
    <g fill="none" stroke="#444" stroke-width="3.5">
      <path d="M265 200V187H282"/><path d="M364 178H371V200"/>
      <path d="M373 280V290H357"/><path d="M269 283V296H286"/>
    </g>
    <g fill="#444">
      <path d="M281 182L289 187L281 192Z"/><path d="M366 199L371 207L376 199Z"/>
      <path d="M358 285L350 290L358 295Z"/><path d="M264 284L269 276L274 284Z"/>
    </g>
    <g font-family="Poppins, sans-serif" font-style="italic" font-size="5" fill="#333" text-anchor="middle">
      <text x="271" y="166">WPS meetings</text>
      <text x="397" y="166">Weekly Peer Support</text><text x="397" y="172">(WPS) meetings</text><text x="397" y="178">(2 hours)</text>
      <text x="271" y="312">WPS meetings</text>
      <text x="376" y="310">WPS meetings</text>
    </g>
  </svg>

  <div class="side-tab" style="left:19px;top:333px;width:55px">WHY</div>
  <div style="left:18px;top:330px;width:2px;height:24px;background:#555"></div>
  <p class="body-text" style="left:24px;top:361px;width:178px;text-align:justify">Many people are not satisfied with their work, but they don't know what to do about it. This Program offers you a safe place to conduct your inner journey with collective support, helping you reflect, design, and (very likely) do something about it. It aims at:</p>
  <p class="body-text" style="left:24px;top:408px">Increasing awareness, clarity and confidence</p>
  <ol class="list" style="left:24px;top:418px;width:170px">
    <li><span class="num num-blue">1</span><span>Having a deeper <b><i>insight</i></b> on what makes you happier and what you want</span></li>
    <li><span class="num num-blue">2</span><span>Developing a clear <b><i>design</i></b> integrating your intended work and life</span></li>
    <li><span class="num num-blue">3</span><span>Start <b><i>executing</i></b> this design</span></li>
  </ol>

  <div class="divider"></div>

  <div class="side-tab" style="left:224px;top:333px;width:53px">HOW</div>
  <div style="left:222px;top:330px;width:2px;height:24px;background:#555"></div>
  <p class="body-text" style="left:229px;top:361px;width:180px">This Program differs from existing venture programs in many ways:</p>
  <ol class="list" style="left:229px;top:378px;width:180px">
    <li><span class="num num-orange">1</span><span>Uses mindfulness and self analysis to look deeply into yourself</span></li>
    <li><span class="num num-orange">2</span><span>Design and execution decisions are based on happiness rather than (only) financials</span></li>
    <li><span class="num num-orange">3</span><span>Holistic and inclusive design process, integrating work and life, and building synergies between your different parts</span></li>
  </ol>
  <p class="body-text" style="left:229px;top:464px;width:180px;text-align:justify">Format includes: lectures, individual work, group sharing, guided activities, experiential exercises, video, audio, handouts and other resources.</p>

  <div class="forest" role="img" aria-label="Forest path with a person walking between tall trees"></div>
  <svg style="left:0;top:495px;width:443px;height:50px" viewBox="0 0 443 50" aria-hidden="true">
    <path d="M0 16Q221 75 443 8V0H0Z" fill="var(--paper)"/>
    <path d="M0 16Q221 75 443 8" fill="none" stroke="var(--blue)" stroke-width="4"/>
  </svg>
  <div class="quote">“The way out is in”</div>

  <div class="back-contact"><b>Email:</b> info@brightfoldjoy.io</div>
  <div class="pill back-pill"><b>Tel:</b> +34 611 482 305 <i>(video call and messaging)</i></div>
</section>

</body>
</html>
```